Yoga By Marisol Ad for print

I need a print ad designed to go in a brochure for a charity event. I've attached the specs. I need the specs for the 1/2 page ad.
Text for ad:

“E-RYT 200 extensive training with Asana Scholars
Social Media Influencer
Offering group, private and corporate yoga classes
Email: info@yogabymarisol-studio.com
Web: www.yogabymarisol-studio.com
Phone: 480-555-0163
Instagram: @flowofmarisol

Target Market(s)

Yoga practitioners and businesses looking to bring yoga in to their operation.

Font styles to use
Serif
Script

Colors
eda3c7
e34197
eea4c8
f9d9e8
feeeee
000000
1b1b1b
cbcbcb
eaeaea

Requirements
Must have
• One version of my logo, I have provided many to choose from for best aesthetic appeal

```html
<!DOCTYPE html>
<html lang="en">
<head>
<meta charset="utf-8">
<title>Yoga By Marisol – Print Ad</title>
<link href="https://fonts.googleapis.com/css2?family=Roboto+Condensed:wght@700&family=Caveat:wght@500&family=Open+Sans:wght@600&display=swap" rel="stylesheet">
<style>
  :root{
    --page-bg:#cbcbcb;
    --pink-deep:#e34197;
    --pink-mid:#eda3c7;
    --pink-light:#f9d9e8;
    --band-dark:#1b1b1b;
    --band-line:#feeeee;
    --magenta:#e34197;
    --ink:#000000;
    --bubble-light:#ffffff;
    --bubble-shade:#eaeaea;
    --bubble-ring:#6f6f6f;
    --photo-top:#c9a58a;
    --photo-bottom:#a9a9ad;
    --contact-text:#ffffff;
    --icon-pink:#eea4c8;
  }
  html,body{margin:0;padding:0;width:1200px;height:1200px;overflow:hidden;background:var(--page-bg);}
  .ad{position:absolute;left:176px;top:20px;width:848px;height:1160px;display:block;box-shadow:0 4px 18px rgba(0,0,0,.35);}
  .bubble-lead{font-family:"Caveat",cursive;font-size:40px;fill:var(--ink);}
  .bubble-copy{font-family:"Roboto Condensed",sans-serif;font-weight:700;font-size:33px;fill:var(--magenta);}
  .brand-name{font-family:"Roboto Condensed",sans-serif;font-weight:700;font-size:33px;fill:var(--magenta);}
  .contact-text{font-family:"Open Sans",sans-serif;font-weight:600;font-size:20px;fill:var(--contact-text);}
  .connector{fill:none;stroke:var(--ink);stroke-width:2;stroke-dasharray:7 6;}
  .contact-icon{fill:none;stroke:var(--icon-pink);stroke-width:2;}
</style>
</head>
<body>
<svg class="ad" viewBox="0 0 846 1158" xmlns="http://www.w3.org/2000/svg">
  <defs>
    <radialGradient id="pink-glow" cx="0.5" cy="0.55" r="0.65">
      <stop offset="0" stop-color="var(--pink-mid)"/>
      <stop offset="1" stop-color="var(--pink-deep)"/>
    </radialGradient>
    <radialGradient id="bubble-fill" cx="0.45" cy="0.4" r="0.65">
      <stop offset="0.4" stop-color="var(--bubble-light)"/>
      <stop offset="1" stop-color="var(--bubble-shade)"/>
    </radialGradient>
    <linearGradient id="photo-fill" x1="0" y1="0" x2="0" y2="1">
      <stop offset="0" stop-color="var(--photo-top)"/>
      <stop offset="1" stop-color="var(--photo-bottom)"/>
    </linearGradient>
  </defs>

  <rect class="ad-background" width="846" height="1158" fill="url(#pink-glow)"/>
  <path class="footer-band" d="M0 878 L846 1008 L846 1158 L0 1158 Z" fill="var(--band-dark)"/>
  <path class="footer-line" d="M0 872 L846 1002" stroke="var(--band-line)" stroke-width="6"/>

  <path class="connector" d="M203 242 Q240 185 300 160"/>
  <path class="connector" d="M572 170 Q625 195 652 246"/>

  <rect class="instructor-photo" x="150" y="238" width="520" height="812" rx="60" fill="url(#photo-fill)" role="img" aria-label="Photo of the instructor kneeling in a yoga pose with hands in prayer position"/>

  <g class="bubble bubble-credential">
    <circle cx="436" cy="150" r="133" fill="url(#bubble-fill)" stroke="var(--bubble-ring)" stroke-width="4"/>
    <text class="bubble-lead" x="436" y="90" text-anchor="middle">I am a</text>
    <text class="bubble-copy" text-anchor="middle">
      <tspan x="436" y="132">E-RYT 200</tspan>
      <tspan x="436" y="173">trained with</tspan>
      <tspan x="436" y="214">Asana Scholars</tspan>
    </text>
  </g>

  <g class="bubble bubble-influencer">
    <circle cx="187" cy="372" r="133" fill="url(#bubble-fill)" stroke="var(--bubble-ring)" stroke-width="4"/>
    <text class="bubble-lead" x="187" y="334" text-anchor="middle">I am a</text>
    <text class="bubble-copy" text-anchor="middle">
      <tspan x="187" y="379">social media</tspan>
      <tspan x="187" y="422">influencer</tspan>
    </text>
  </g>

  <g class="bubble bubble-classes">
    <circle cx="680" cy="373" r="133" fill="url(#bubble-fill)" stroke="var(--bubble-ring)" stroke-width="4"/>
    <text class="bubble-lead" x="680" y="313" text-anchor="middle">I offer</text>
    <text class="bubble-copy" text-anchor="middle">
      <tspan x="680" y="355">Group, Private</tspan>
      <tspan x="680" y="396">and Corporate</tspan>
      <tspan x="680" y="437">yoga classes</tspan>
    </text>
  </g>

  <g class="bubble bubble-brand">
    <circle cx="701" cy="905" r="108" fill="url(#bubble-fill)" stroke="var(--bubble-ring)" stroke-width="4"/>
    <text class="brand-name" x="701" y="917" text-anchor="middle">Marisol Flow</text>
  </g>

  <g class="contact contact-email">
    <rect x="46" y="1077" width="20" height="14" fill="var(--icon-pink)"/>
    <path d="M46 1077 L56 1086 L66 1077" fill="none" stroke="var(--band-dark)" stroke-width="2"/>
    <text class="contact-text" x="78" y="1091">info@yogabymarisol-studio.com</text>
  </g>
  <g class="contact contact-web">
    <g class="contact-icon">
      <circle cx="460" cy="1084" r="9"/>
      <ellipse cx="460" cy="1084" rx="4" ry="9"/>
      <path d="M451 1084 H469 M453 1079 H467 M453 1089 H467"/>
    </g>
    <text class="contact-text" x="478" y="1091">www.yogabymarisol-studio.com</text>
  </g>
  <g class="contact contact-phone">
    <path d="M48 1113 q2 -3 5 -1 l3 4 q1 2 -1 3 l-2 1 q2 5 7 7 l1 -2 q1 -2 3 -1 l4 3 q2 3 -1 5 q-4 3 -10 -1 q-7 -5 -10 -11 q-2 -4 1 -7 z" fill="var(--icon-pink)"/>
    <text class="contact-text" x="78" y="1129">480-555-0163</text>
  </g>
  <g class="contact contact-social">
    <path class="contact-icon" d="M451 1114 h18 v12 h-11 l-5 4 v-4 h-2 z"/>
    <text class="contact-text" x="478" y="1129">@flowofmarisol</text>
  </g>
</svg>
</body>
</html>
```